Used Car Dealer seeks an Amazing Business Card Design

We are looking for a business card design that incorporates our logo and grabs the attention of anyone we give the business card to.

Looking to use the same colors as the logo. Our Logo choice is the black background with Red and Silver/Grey Lettering.

We also would like to see some embossed designs.

Target Market(s)

Used Car Buyers, Automotive, Auto

Industry/Entity Type

Automotive

Contact Information for Business Card

BVEL7K
Gordon Whitlock
482 Tarrow Lane
Suite 207
Brennick, GA 31948
Office (770) 555-0142
Cell (770) 555-0187
bvel7kga@quellmail.com
www.bvel7kga.com

Colors
ffffff
ee3036

Requirements
Must have
• Must include our logo (Black Background with Red and Silver/Grey Lettering)
Nice to have
• Embossed Design. Can be Single or Double Sided.

```html
<!DOCTYPE html>
<html lang="en">
<head>
<meta charset="utf-8">
<title>BVEL7K Business Card</title>
<link href="https://fonts.googleapis.com/css2?family=Open+Sans:wght@400;600&display=swap" rel="stylesheet">
<style>
  :root {
    --page-bg: #e9e7e4;
    --card-black: #0e0d10;
    --card-grey: #2a282d;
    --brand-red: #ee3036;
    --brand-red-dark: #b5181d;
    --notch-dark: #1c1b1f;
    --text-white: #ffffff;
    --silver: #c9c9cc;
  }
  * { box-sizing: border-box; margin: 0; padding: 0; }
  html, body { width: 1200px; height: 1200px; overflow: hidden; }
  body {
    background: var(--page-bg);
    font-family: "Open Sans", sans-serif;
    display: flex; align-items: center; justify-content: center;
  }
  .business-card {
    position: relative;
    width: 1000px; height: 572px;
    background: radial-gradient(ellipse at 55% 55%, var(--card-grey) 0%, var(--card-black) 70%);
    overflow: hidden;
    box-shadow: 0 14px 40px rgba(0,0,0,.25);
  }
  .card-bands { position: absolute; inset: 0; width: 100%; height: 100%; }
  .contact-list {
    position: absolute; left: 70px; top: 95px;
    list-style: none; color: var(--text-white);
  }
  .contact-item {
    display: flex; align-items: center; gap: 22px;
    font-size: 18px; line-height: 1.4;
    margin-bottom: 34px;
  }
  .contact-icon {
    width: 44px; height: 44px; flex: none;
    border: 2px solid var(--text-white);
    display: flex; align-items: center; justify-content: center;
  }
  .contact-icon svg { width: 28px; height: 28px; }
  .holder-name {
    position: absolute; right: 80px; top: 150px;
    color: var(--text-white); font-size: 27px; font-weight: 400;
    letter-spacing: 1px; text-transform: uppercase;
  }
  .brand {
    position: absolute; left: 520px; top: 280px;
    display: flex; align-items: center; gap: 18px;
  }
  .brand-dot { width: 22px; height: 22px; border-radius: 50%; background: var(--brand-red); flex: none; }
  .brand-name {
    font-size: 74px; font-weight: 600; color: var(--silver);
    letter-spacing: 2px; line-height: 1;
  }
</style>
</head>
<body>
  <article class="business-card">
    <svg class="card-bands" viewBox="0 0 1000 572" preserveAspectRatio="none" aria-hidden="true">
      <rect x="0" y="0" width="1000" height="20" fill="var(--brand-red)"/>
      <polygon points="520,20 760,20 735,48 545,48" fill="var(--brand-red)"/>
      <polygon points="560,20 720,20 705,36 575,36" fill="var(--notch-dark)"/>
      <rect x="760" y="20" width="240" height="10" fill="var(--brand-red-dark)"/>
      <rect x="0" y="528" width="1000" height="44" fill="var(--brand-red)"/>
      <polygon points="300,528 560,528 585,500 275,500" fill="var(--brand-red)"/>
      <polygon points="320,528 540,528 555,512 305,512" fill="var(--notch-dark)"/>
      <rect x="0" y="514" width="275" height="14" fill="var(--brand-red-dark)"/>
    </svg>

    <ul class="contact-list">
      <li class="contact-item">
        <span class="contact-icon">
          <svg viewBox="0 0 24 24" fill="none" stroke="#fff" stroke-width="1.8"><rect x="7" y="2" width="10" height="20" rx="2"/><line x1="11" y1="18.5" x2="13" y2="18.5"/></svg>
        </span>
        <span>Office (770) 555-0142<br>Cell (770) 555-0187</span>
      </li>
      <li class="contact-item">
        <span class="contact-icon">
          <svg viewBox="0 0 24 24" fill="none" stroke="#fff" stroke-width="1.6"><circle cx="12" cy="12" r="9"/><ellipse cx="12" cy="12" rx="4" ry="9"/><line x1="3" y1="12" x2="21" y2="12"/><line x1="5" y1="7" x2="19" y2="7"/><line x1="5" y1="17" x2="19" y2="17"/></svg>
        </span>
        <span>www.bvel7kga.com</span>
      </li>
      <li class="contact-item">
        <span class="contact-icon">
          <svg viewBox="0 0 24 24" fill="none" stroke="#fff" stroke-width="1.6"><rect x="3" y="5" width="18" height="14"/><polyline points="3,5 12,13 21,5"/></svg>
        </span>
        <span>bvel7kga@quellmail.com</span>
      </li>
      <li class="contact-item">
        <span class="contact-icon">
          <svg viewBox="0 0 24 24" fill="#fff"><polygon points="12,3 22,12 19,12 19,21 5,21 5,12 2,12"/><rect x="9" y="14" width="6" height="5" fill="#0e0d10"/></svg>
        </span>
        <span>482 Tarrow Lane, Suite 207<br>Brennick, GA 31948</span>
      </li>
    </ul>

    <h1 class="holder-name">Gordon Whitlock</h1>

    <div class="brand">
      <span class="brand-dot"></span>
      <span class="brand-name">BVEL7K</span>
    </div>
  </article>
</body>
</html>
```